UK Based Internet hosting Company wants a vibrant eCommerce site designed.

We have only just had our logo and brand designed by Pixel Forum which went so well that we would like to open up our website design project on here too.

The company is called 'Quay Server Lantern' and we provide a range of website hosting, dedicated server, domain name and email solutions that people will be able to purchase online in neatly packaged options from the outset.

Our logo and brand is bright turquoise, black & white (samples of branding will be attached with this project) but we would like the website to be very vibrant with good use of white space rather than a black website.

We want to appeal to end users so web designers, developers and people who would like to host their website. But we also want to appeal to resellers that would like to resell our hosting packages too.

We want a big push on social media and blogging on the site as we would like our brand to be 100% up with Chatterleaf, Murmel, workLoop, Vidplume and Zorbix+. It would be great to have this integrated into the site with share buttons and rating buttons etc.

We would like to see a homepage initially with a view to providing several page layers down to help our in-house developers hook in our back-end into this front end effectively.

Great customer experience and an easy to navigate journey to the checkout when purchasing the hosting packages is paramount !!

We like how the following sites are set-out and presented:

www.brightmarrow.uk
http://www.tallyfold.co.uk
https://www.qv7.net/web-hosting/

Target Market(s)

We have 3 target markets.

Target market 1 - end users, consumers such as Web Designers, Developers and small businesses.

Target Market 2 - Resellers, small businesses that would like to resell our services.

Target Market 3 - Medium to large businesses that would like more of a bespoke solution.

Industry/Entity Type

Internet

Requirements
Must have
• Colourful, bright, bold, easy to navigate and to purchase packages.
• Plenty of call to actions, social media, ratings.
• Video case studies and testimonials would be nice.

```html
<!DOCTYPE html>
<html lang="en">
<head>
<meta charset="utf-8">
<title>Quay Server Lantern – Web Hosting</title>
<link rel="stylesheet" href="https://fonts.googleapis.com/css2?family=Open+Sans:wght@400;600;700;800&display=swap">
<style>
:root{
  --teal:#2cb89a;
  --teal-dark:#239a80;
  --ink:#222;
  --text:#555;
  --muted:#888;
  --dark:#1d1d1d;
  --footer:#2a2a2a;
  --footer-deep:#1a1a1a;
  --white:#fff;
  --line:#e3e3e3;
}
*{box-sizing:border-box;margin:0;padding:0}
html,body{width:1200px;height:4316px;overflow:hidden}
body{font-family:"Open Sans",Arial,sans-serif;color:var(--text);background:var(--white);position:relative}
section,header,footer,nav{position:absolute;left:0;width:1200px}
a{color:inherit;text-decoration:none}
.btn{display:inline-block;background:var(--teal);color:var(--white);font-weight:700;text-transform:uppercase}

/* top bar */
.topbar{top:0;height:36px;background:var(--dark);color:#ccc;font-size:13px}
.topbar .support{position:absolute;left:0;top:0;height:36px;padding:0 16px;background:var(--teal);color:#fff;line-height:36px;font-weight:600}
.topbar .contact{position:absolute;left:120px;top:0;line-height:36px}
.topbar .contact span{margin-right:22px}
.topbar .account{position:absolute;right:0;top:0;line-height:36px}
.topbar .account span{display:inline-block;padding:0 14px;height:36px}
.topbar .account .signup{background:var(--teal);color:#fff}
.brand{position:absolute;left:480px;top:0;width:240px;height:72px;background:var(--white);border-radius:0 0 10px 10px;display:flex;align-items:center;justify-content:center;gap:10px;z-index:3}
.brand i{width:34px;height:34px;border-radius:50%;background:var(--teal);display:block}
.brand b{font-size:19px;color:var(--ink);font-weight:700;line-height:1.05;width:140px}

/* hero */
.hero{top:36px;height:524px;background:linear-gradient(180deg,#0d1a22 0%,#1a3440 55%,#0e1c24 100%)}
.hero .servers{position:absolute;right:60px;top:60px;width:640px;height:420px;background:linear-gradient(90deg,#1d4f63,#3b93b3 60%,#1f5568);opacity:.85;border-radius:4px}
.hero .copy{position:absolute;left:190px;top:190px;color:#fff}
.hero h1{font-size:34px;font-weight:600;line-height:1.1}
.hero h2{font-size:40px;font-weight:800;color:var(--teal);text-transform:uppercase;line-height:1.15}
.hero p{font-size:14px;margin:6px 0 18px}
.hero .btn{padding:12px 24px;font-size:15px}
.hero .from{font-size:13px;margin-top:10px;color:#ddd}
.arrow{position:absolute;top:50%;width:36px;height:36px;border-radius:50%;background:#fff;margin-top:-18px}
.arrow svg{display:block;width:36px;height:36px}

/* nav */
.mainnav{top:560px;height:46px;background:var(--teal)}
.mainnav ul,.bottomnav ul{list-style:none;display:flex;padding-left:40px}
.mainnav li{color:#fff;font-size:17px;line-height:46px;padding:0 22px;text-transform:uppercase}
.mainnav li.active{background:#fff;color:var(--teal)}

/* features */
.features{top:606px;height:410px;display:flex;justify-content:space-around;padding:0 70px}
.feature{width:300px;text-align:center;padding-top:130px}
.feature h3{font-size:20px;font-weight:800;color:var(--ink);text-transform:uppercase;line-height:1.2;margin-bottom:24px}
.feature p{font-size:15px;line-height:1.6}

/* domain search */
.domain{top:1016px;height:420px;background:linear-gradient(180deg,#2b1d18 0%,#4a3226 45%,#1f1815 100%);text-align:center;color:#fff}
.domain h2{font-size:40px;font-weight:400;margin-top:100px}
.domain .from{font-size:18px;margin-top:4px}
.search{width:700px;height:44px;margin:16px auto 0;display:flex}
.search div{flex:1;background:#fff}
.search span{width:80px;background:var(--teal);line-height:44px;font-weight:700}
.tlds{display:flex;flex-wrap:wrap;width:420px;margin:18px auto 0;gap:14px 60px;justify-content:center}
.tlds span{background:var(--teal);padding:2px 12px;font-size:14px}

/* plans */
.plans{top:1436px;height:580px;text-align:center}
.section-title{font-size:40px;font-weight:800;color:var(--ink);padding-top:60px}
.section-sub{font-size:17px;color:#666}
.plan-row{display:flex;justify-content:center;gap:50px;margin-top:36px}
.plan{width:220px;text-align:left}
.plan .icon{width:110px;height:110px;margin:0 auto 14px;display:block}
.plan h3{font-size:26px;color:var(--ink);font-weight:600}
.plan p{font-size:14px;line-height:1.4;height:40px}
.plan .price{font-size:32px;color:var(--ink);margin-top:18px}
.plan .price sup{font-size:15px}
.plan .vat{font-size:13px;color:var(--muted)}
.plan .btn{width:200px;text-align:center;padding:8px 0;font-size:20px;font-weight:600;text-transform:none;margin-top:12px}

/* testimonials */
.testimonials{top:2016px;height:520px;text-align:center}
.testimonials .section-title{font-size:34px;padding-top:20px}
.rating{font-size:15px}
.rating em{color:var(--teal);font-style:normal}
.avatar{width:130px;height:130px;border-radius:50%;background:radial-gradient(circle,#cfcfcf,#8a8a8a);margin:22px auto 0}
.quote{font-size:15px;width:760px;margin:70px auto 0;line-height:1.5}
.quote em{color:var(--teal);font-style:normal}
.author{margin-top:30px;font-size:16px;color:var(--ink)}
.role{font-size:13px}
.dots{display:flex;gap:8px;justify-content:center;margin-top:18px}
.dots i{width:12px;height:12px;border-radius:50%;background:#bbb}
.dots i:first-child{background:#555}

/* blog */
.blog{top:2536px;height:590px;text-align:center}
.blog .section-title{font-size:34px;padding-top:10px}
.posts{display:flex;gap:30px;justify-content:center;margin-top:40px;text-align:left}
.post{width:355px}
.post .thumb{height:150px}
.post h4{font-size:19px;color:var(--ink);font-weight:600;margin-top:20px;line-height:1.25}
.post .meta{font-size:13px;color:var(--teal);margin:8px 0}
.post p{font-size:14px;line-height:1.45}

/* social */
.social{top:3126px;height:470px;background:linear-gradient(180deg,#3a3a3a,#151515)}
.social h2{position:absolute;left:0;width:100%;top:26px;text-align:center;color:#fff;font-size:34px;font-weight:700}
.stats{position:absolute;top:115px;left:0;width:100%;display:flex;justify-content:center;gap:130px}
.stat{width:180px;height:180px;border-radius:50%;background:rgba(40,40,40,.85);border:6px solid var(--teal);color:#fff;text-align:center;padding-top:44px}
.stat b{font-size:40px;font-weight:400;display:block;line-height:1}
.stat small{font-size:13px}
.stat span{display:inline-block;background:#4a6db3;font-size:13px;padding:2px 12px;margin-top:8px;font-weight:700}

/* clients */
.clients{top:3596px;height:330px;text-align:center}
.clients .section-title{font-size:34px;padding-top:50px}
.logos{display:flex;justify-content:center;gap:60px;margin-top:60px;align-items:center}
.logos span{font-size:22px;font-weight:700;color:var(--ink);display:flex;align-items:center;gap:8px}
.logos i{width:22px;height:22px;background:var(--ink);border-radius:50%;display:block}

/* footer */
.footer{top:3926px;height:312px;background:var(--footer);color:#ddd}
.footer .col{position:absolute;top:36px}
.footer h5{font-size:28px;color:#fff;font-weight:600;text-align:center;margin-bottom:20px}
.footer p{font-size:15px;line-height:1.5}
.footer .contact-list li{list-style:none;font-size:15px;line-height:1.9}
.footer .contact-list b{color:var(--teal)}
.follow{display:flex;flex-wrap:wrap;gap:12px;width:200px;justify-content:center}
.follow i{width:44px;height:44px;border-radius:50%;border:2px solid #888;display:block}
.subscribe{display:flex;margin-top:20px;width:220px}
.subscribe div{flex:1;background:#fff;height:32px}
.subscribe span{background:var(--teal);color:#fff;font-weight:700;padding:0 10px;line-height:32px}
.copyright{position:absolute;bottom:14px;width:100%;text-align:center;font-size:12px;color:#999}
.bottomnav{top:4238px;height:78px;background:var(--footer-deep)}
.bottomnav ul{justify-content:center;padding:0}
.bottomnav li{color:#fff;font-size:18px;line-height:78px;padding:0 24px;text-transform:uppercase}
</style>
</head>
<body>

<header class="topbar">
  <span class="support">&#9679; Support</span>
  <div class="contact"><span>&#9993; Email Us</span><span>&#9742; 07700 900 127</span></div>
  <div class="account"><span>&#128274; Login</span><span class="signup">Sign up</span></div>
</header>
<a class="brand" href="#"><i></i><b>Quay Server Lantern</b></a>

<section class="hero">
  <div class="servers" role="img" aria-label="Photo of rows of blue-lit server racks"></div>
  <div class="copy">
    <h1>Your website deserves</h1>
    <h2>Great Web Hosting</h2>
    <p>The UK's best web hosting backed by free 24x7 support</p>
    <a class="btn" href="#">View our packages</a>
    <div class="from">From Only &euro; 2.15/m</div>
  </div>
  <span class="arrow" style="left:60px"><svg viewBox="0 0 36 36"><path d="M21 11l-7 7 7 7" fill="none" stroke="#222" stroke-width="3"/></svg></span>
  <span class="arrow" style="right:60px"><svg viewBox="0 0 36 36"><path d="M15 11l7 7-7 7" fill="none" stroke="#222" stroke-width="3"/></svg></span>
</section>

<nav class="mainnav">
  <ul><li class="active">Home</li><li>Company</li><li>Domine Names</li><li>Reseller Hosting</li><li>Blog</li><li>Resources</li><li>Kudos</li><li>Contact</li></ul>
</nav>

<section class="features">
  <div class="feature"><h3>World's leading domain registrar</h3><p>We have 100s of domains to choose from, not to mention prices that other companies only dream about.</p></div>
  <div class="feature"><h3>More names at better prices</h3><p>We have 100s of domains to choose from, not to mention prices that other companies only dream about.</p></div>
  <div class="feature"><h3>Award-winning 24/7 support</h3><p>We have 100s of domains to choose from, not to mention prices that other companies only dream about.</p></div>
</section>

<section class="domain" role="img" aria-label="Night city street photo behind domain search">
  <h2>Get the Domain of Your Dream</h2>
  <div class="from">From Only &euro; 2.15/m</div>
  <div class="search"><div></div><span>Search</span></div>
  <div class="tlds"><span>.net</span><span>.org</span><span>.co</span><span>.com</span><span>.biz</span></div>
</section>

<section class="plans">
  <h2 class="section-title">Different hosting platforms to suit every need!</h2>
  <p class="section-sub">Each type of hosting service we provide is further optimised with unique performance tweaks!</p>
  <div class="plan-row">
    <div class="plan">
      <svg class="icon" viewBox="0 0 110 110"><circle cx="55" cy="55" r="50" fill="none" stroke="var(--teal)" stroke-width="5"/><path d="M32 62a12 12 0 0 1 6-22 17 17 0 0 1 32-2 12 12 0 0 1 8 24z" fill="var(--teal)"/><path d="M55 62v14M40 76h30" stroke="var(--teal)" stroke-width="4"/></svg>
      <h3>Web Hosting</h3><p>Fast, reliable &amp; secure cloud web hosting with UK support.</p>
      <div class="price">&pound;2.<sup>15/M</sup></div><div class="vat">excluding VAT at 20%</div>
      <a class="btn" href="#">Find Out More</a>
    </div>
    <div class="plan">
      <svg class="icon" viewBox="0 0 110 110"><circle cx="55" cy="55" r="50" fill="none" stroke="var(--teal)" stroke-width="5"/><path d="M30 72l-4-32 16 14 13-20 13 20 16-14-4 32z" fill="var(--teal)"/><rect x="30" y="76" width="50" height="6" fill="var(--teal)"/></svg>
      <h3>Premium Hosting</h3><p>High performance server power hosting managed by us.</p>
      <div class="price">&pound;2.<sup>15/M</sup></div><div class="vat">excluding VAT at 20%</div>
      <a class="btn" href="#">Find Out More</a>
    </div>
    <div class="plan">
      <svg class="icon" viewBox="0 0 110 110"><circle cx="55" cy="55" r="50" fill="none" stroke="var(--teal)" stroke-width="5"/><path d="M28 50l14-14 14 10 14-10 14 14-26 26z" fill="none" stroke="var(--teal)" stroke-width="5" stroke-linejoin="round"/></svg>
      <h3>Reseller</h3><p>Profit with the UK's most advanced reseller hosting.</p>
      <div class="price">&pound;2.<sup>15/M</sup></div><div class="vat">excluding VAT at 20%</div>
      <a class="btn" href="#">Find Out More</a>
    </div>
    <div class="plan">
      <svg class="icon" viewBox="0 0 110 110"><path d="M20 80a40 40 0 1 1 70 0" fill="none" stroke="var(--teal)" stroke-width="12"/><path d="M55 70l16-26" stroke="var(--teal)" stroke-width="6" stroke-linecap="round"/><circle cx="55" cy="70" r="7" fill="var(--teal)"/></svg>
      <h3>VPS</h3><p>Boost your website with a custom VPS.</p>
      <div class="price">&pound;2.<sup>15/M</sup></div><div class="vat">excluding VAT at 20%</div>
      <a class="btn" href="#">Find Out More</a>
    </div>
  </div>
</section>

<section class="testimonials">
  <h2 class="section-title">What Our Customer Say About Us</h2>
  <p class="rating">We are rated 4.98 / 5.00 <em>Based on 400 Trustmark Reviews</em></p>
  <div class="avatar" role="img" aria-label="Customer portrait photo"></div>
  <p class="quote">They're smart: they ask the right questions and come up with great suggestions or alternatives for what you are trying to do. <em>Read More</em></p>
  <p class="author">Rowan Pell</p>
  <p class="role">CEO</p>
  <div class="dots"><i></i><i></i><i></i><i></i></div>
</section>

<section class="blog">
  <h2 class="section-title">Lasted blog post</h2>
  <p class="section-sub">Our style of business is simple and straightforward.</p>
  <div class="posts">
    <article class="post"><div class="thumb" role="img" aria-label="Photo of a hand touching glowing network icons" style="background:linear-gradient(135deg,#1b2a3a,#5a7794)"></div><h4>Tips in Ten: Addressing customers' perceived risk</h4><p class="meta">By : Matthew | Jul 01, 2015 | 0 Comments</p><p>For the first time ever, we're revealing our own internal business and website tips and best practices through our Tips in Ten series. Designed to introduce new topics and provide practical advice</p></article>
    <article class="post"><div class="thumb" role="img" aria-label="Photo of hands over a laptop keyboard" style="background:linear-gradient(180deg,#dbe6f2,#9fb3c8)"></div><h4>3 more ways to power up your knowledge</h4><p class="meta">By : Matthew | Jul 01, 2015 | 0 Comments</p><p>For the first time ever, we're revealing our own internal business and website tips and best practices through our Tips in Ten series. Designed to introduce new topics and provide practical advice</p></article>
    <article class="post"><div class="thumb" role="img" aria-label="Photo of business people meeting at a desk" style="background:linear-gradient(135deg,#7d8fa3,#e1e6ec)"></div><h4>Tips in Ten: Addressing customers' perceived risk</h4><p class="meta">By : Matthew | Jul 01, 2015 | 0 Comments</p><p>For the first time ever, we're revealing our own internal business and website tips and best practices through our Tips in Ten series. Designed to introduce new topics and provide practical advice</p></article>
  </div>
</section>

<section class="social" role="img" aria-label="Black and white photo of a group of people behind social stats">
  <h2>Chatterleaf</h2>
  <span class="arrow" style="left:30px;background:none"><svg viewBox="0 0 36 36"><path d="M21 11l-7 7 7 7" fill="none" stroke="#fff" stroke-width="3"/></svg></span>
  <span class="arrow" style="right:30px;background:none"><svg viewBox="0 0 36 36"><path d="M15 11l7 7-7 7" fill="none" stroke="#fff" stroke-width="3"/></svg></span>
  <div class="stats">
    <div class="stat"><b>8564</b><small>people like</small><br><span>Like</span></div>
    <div class="stat"><b>8564</b><small>people share</small><br><span>Like</span></div>
    <div class="stat"><b>8564</b><small>people comment</small><br><span>Like</span></div>
  </div>
</section>

<section class="clients">
  <h2 class="section-title">Some of Our Clients</h2>
  <p class="section-sub">Our style of business is simple and straightforward.</p>
  <div class="logos">
    <span><i></i>Summitvale</span><span><i></i>Starbrook</span><span><i></i>Voltera</span><span><i></i>Mangrove</span><span><i></i>Betalune</span>
  </div>
</section>

<footer class="footer">
  <div class="col" style="left:40px;width:320px"><h5>About Us</h5><p>For the first time ever, we're revealing our own internal business and website tips and best practices through our Tips in Ten series. Designed to introduce new topics and provide practical advice</p></div>
  <div class="col" style="left:470px;width:340px"><h5>Contact us</h5>
    <ul class="contact-list"><li><b>&#9993; E-Mail Us :</b> david@quayserverlantern.com</li><li><b>&#9742; Call Us at :</b> 07700 900 127 · 0800 160 0418</li><li><b>&#9906; Location :</b> Quay Server Lantern UK</li></ul></div>
  <div class="col" style="left:930px;width:220px"><h5>Follow Us</h5>
    <div class="follow" aria-label="Social links: Chatterleaf, Murmel, workLoop, Zorbix+, Vidplume"><i></i><i></i><i></i><i></i><i></i></div>
    <div class="subscribe"><div></div><span>GO</span></div>
  </div>
  <p class="copyright">&copy; 2015 Quay Server Lantern. All rights reserved.</p>
</footer>

<nav class="bottomnav">
  <ul><li>Home</li><li>Company</li><li>Domine Names</li><li>Reseller Hosting</li><li>Blog</li><li>Resources</li><li>Kudos</li><li>Contact</li></ul>
</nav>

</body>
</html>
```